New Cloud Backups MSP - Online Backups - DR - IT Support

My new MSP company offers low cost IT Support and online backups and DR using VaultMerrin solutions.

Some examples of competitors would include;

http://www.trelvonix.example.au/
http://www.quarnidata.example.au/

We require a designer to work closely with us to develop and implement a new website with a signup portal for customers, costing calculators and just general information.

If possible we would also like a new logo designed to complement the new website (as an additional cost)

Target Market(s)

Companies looking for online backups
Companies looking for cost effective IT support

Industry/Entity Type

It Company

Font styles to use
Sans Serif

Colors

Designer to choose colors to be used in the design.

Requirements
Must have
• 'Menu' of services offered
Request a quote form

```html
<!DOCTYPE html>
<html lang="en">
<head>
<meta charset="utf-8">
<title>Harlowe Cloud – A MSP Company</title>
<link href="https://fonts.googleapis.com/css2?family=Open+Sans:wght@400;600&display=swap" rel="stylesheet">
<style>
:root{
  --blue:#2b7ab8;
  --nav-blue:#3a87c4;
  --green:#5fae2e;
  --text:#333;
  --muted:#777;
  --line:#dcdcdc;
  --band:#eeeeee;
  --footer:#2b2b2b;
  --footer-text:#b5b5b5;
}
*{box-sizing:border-box;margin:0;padding:0}
html,body{width:986px;height:1200px;overflow:hidden;background:#fff}
body{position:relative;font-family:'Open Sans',Arial,sans-serif;color:var(--text)}
.abs{position:absolute}

.brand{left:82px;top:14px;text-align:right}
.brand-name{font-size:31px;font-weight:600;color:var(--blue);letter-spacing:.5px;line-height:1.1}
.brand-tag{font-size:11px;color:#666;margin-top:2px}
.call{right:82px;top:24px;display:flex;align-items:center;gap:8px}
.call-text{text-align:right}
.call-label{font-size:13px;color:#666}
.call-number{font-size:19px;color:#333;line-height:1.1}

.band{left:0;top:105px;width:986px;height:336px;background:var(--band)}

.nav{left:81px;top:87px;width:823px;height:39px;background:var(--nav-blue);display:flex;align-items:center}
.nav a{height:39px;display:flex;align-items:center;padding:0 15px;color:#fff;font-size:12.5px;text-decoration:none;border-right:1px solid rgba(255,255,255,.25)}
.nav a.active{background:var(--green);padding:0 18px}
.search{margin-left:auto;margin-right:6px;width:158px;height:28px;background:#fff;display:flex;align-items:center;justify-content:space-between;padding:0 6px 0 10px;font-size:11.5px;color:#777}

.hero{left:81px;top:133px;width:823px;height:296px;background:linear-gradient(180deg,#1f4fa6 0%,#3d78c8 45%,#b7cfe8 75%,#eef3f8 100%)}
.hero-arrow{left:92px;top:267px}
.hero-title{left:548px;top:216px;width:327px;height:41px;background:rgba(255,255,255,.78);font-size:22px;display:flex;align-items:center;justify-content:center;color:#222}
.hero-desc{left:510px;top:263px;width:365px;height:50px;background:rgba(255,255,255,.72);font-size:11px;text-align:right;padding:7px 18px 0 10px;line-height:19px;color:#222}

.welcome-title{left:84px;top:467px;font-size:22px;color:var(--blue);font-weight:400}
.welcome-text{left:84px;top:502px;width:590px;font-size:11.2px;line-height:19px;color:#444}
.welcome-img{left:691px;top:473px;width:212px;height:118px;background:linear-gradient(135deg,#0d3f8f,#4aa0e6 55%,#cfe6f7)}

.rule{left:82px;width:822px;height:1px;background:var(--line)}

.service{width:260px}
.service-head{display:flex;align-items:center;gap:8px;height:44px}
.service-title{font-size:18px;color:var(--blue)}
.service-text{margin-top:14px;font-size:11.3px;line-height:17px;color:var(--muted)}

.partners{left:82px;top:958px;width:822px;display:flex;justify-content:space-between;align-items:center;font-size:15px;font-weight:600;color:#555;padding:0 12px}

.news{left:0;top:1014px;width:986px;height:51px;background:#ececec}
.news-label{left:82px;top:1014px;width:128px;height:51px;background:#d6d6d6;font-size:15px;display:flex;align-items:center;justify-content:center;color:#333}
.news-label::after{content:"";position:absolute;right:-9px;top:17px;border:9px solid transparent;border-right:0;border-left-color:#d6d6d6}
.news-text{left:240px;top:1022px;font-size:11.2px;line-height:17px;color:#333}
.news-date{color:#999;margin-left:6px}
.news-next{left:881px;top:1029px}

.footer{left:0;top:1065px;width:986px;height:135px;background:var(--footer)}
.footer-links{left:83px;top:1092px;font-size:11px;color:var(--footer-text)}
.footer-links span{margin:0 6px}
.copyright{left:83px;top:1122px;font-size:10.5px;color:var(--footer-text)}
.social{left:84px;top:1155px;display:flex;gap:7px}
.social i{width:21px;height:21px;border-radius:50%;background:#777;display:block}
.vendor{left:728px;top:1135px;font-size:24px;color:#999;letter-spacing:.5px;display:flex;align-items:center;gap:8px}
.vendor i{width:14px;height:14px;border-radius:50%;background:#999;display:block}
</style>
</head>
<body>

<header>
  <div class="abs brand">
    <div class="brand-name">Harlowe Cloud</div>
    <div class="brand-tag">A MSP COMPANY</div>
  </div>
  <div class="abs call">
    <div class="call-text">
      <div class="call-label">Call us Today!</div>
      <div class="call-number">555 014 2290</div>
    </div>
    <svg width="28" height="28" viewBox="0 0 28 28" aria-hidden="true">
      <path d="M5 16 V13 a9 9 0 0 1 18 0 V16" fill="none" stroke="#555" stroke-width="2.5"/>
      <rect x="3" y="15" width="6" height="9" rx="2" fill="#555"/>
      <rect x="19" y="15" width="6" height="9" rx="2" fill="#555"/>
    </svg>
  </div>
</header>

<div class="abs band"></div>

<nav class="abs nav">
  <a class="active">HOME</a>
  <a>ABOUT US</a>
  <a>IT SERVICES</a>
  <a>BACKUP SOLUTIONS</a>
  <a>NEWS</a>
  <a>FAQ'S</a>
  <a>CONTACT US</a>
  <div class="search">Search
    <svg width="16" height="16" viewBox="0 0 16 16" aria-hidden="true"><circle cx="6.5" cy="6.5" r="5" fill="none" stroke="#888" stroke-width="1.8"/><path d="M10 10 L15 15" stroke="#888" stroke-width="2"/></svg>
  </div>
</nav>

<section>
  <div class="abs hero" role="img" aria-label="Glass globe on white blocks against a blue sky with clouds"></div>
  <svg class="abs hero-arrow" width="28" height="28" viewBox="0 0 28 28" aria-hidden="true"><circle cx="14" cy="14" r="14" fill="rgba(90,110,140,.6)"/><path d="M16 8 L10 14 L16 20" fill="none" stroke="#fff" stroke-width="3"/></svg>
  <div class="abs hero-title">Morbi sit amet auctor dolor</div>
  <div class="abs hero-desc">Nam tincidunt faucibus tristique. Proin adipiscing aliquam quam.<br>Curabitur non nisl ut enim euismod venenatis.</div>
</section>

<section>
  <h1 class="abs welcome-title">Welcome to Harlowe cloud</h1>
  <p class="abs welcome-text">Aliquam interdum tincidunt erat ac gravida. Nam ut libero viverra, egestas mauris a, suscipit nunc. Phasellus ullamcorper bibendum diam, eget molestie enim. Vivamus pellentesque mi vitae elit fringilla, ac eleifend dui suscipit. Suspendisse dignissim placerat erat, eu bibendum nunc iaculis eget. Suspendisse cursus massa sit amet turpis mollis volutpat. Proin in lectus dolor. usce lectus dui, condimentum ut aliquam quis, elementum nec nibh. Aliquam viverra enim et nibh pharetra, ac placerat neque volutpat.</p>
  <div class="abs welcome-img" role="img" aria-label="Laptop in a blue digital tunnel"></div>
</section>

<div class="abs rule" style="top:627px"></div>

<section>
  <div class="abs service" style="left:90px;top:654px">
    <div class="service-head">
      <svg width="42" height="42" viewBox="0 0 42 42" aria-hidden="true"><circle cx="21" cy="21" r="19" fill="#2e77b6"/><circle cx="21" cy="21" r="19" fill="none" stroke="#1d5a91" stroke-width="2"/><path d="M9 14 q6 -2 9 3 q-1 5 -6 6 z M24 10 q8 2 9 10 q-5 1 -7 -3 z M20 28 q6 -1 9 4 q-5 5 -10 2 z" fill="#d8e8f5"/></svg>
      <span class="service-title">IT Services</span>
    </div>
    <p class="service-text">Aenean libero sapien, tempus quis adipiscing nec, hendrerit tincidunt ante. Integer vestibulum eros eu ipsum suscipit.</p>
  </div>
  <div class="abs service" style="left:367px;top:654px">
    <div class="service-head">
      <svg width="34" height="42" viewBox="0 0 34 42" aria-hidden="true"><rect x="1" y="1" width="32" height="40" fill="#2e77b6" stroke="#1d5a91" stroke-width="2"/><rect x="5" y="6" width="24" height="13" fill="#5b9bd0"/><rect x="5" y="23" width="24" height="13" fill="#5b9bd0"/><rect x="13" y="11" width="8" height="3" fill="#fff"/><rect x="13" y="28" width="8" height="3" fill="#fff"/></svg>
      <span class="service-title">Storage Service</span>
    </div>
    <p class="service-text">Aenean libero sapien, tempus quis adipiscing nec, hendrerit tincidunt ante. Integer vestibulum eros eu ipsum suscipit.</p>
  </div>
  <div class="abs service" style="left:637px;top:654px">
    <div class="service-head">
      <svg width="44" height="44" viewBox="0 0 44 44" aria-hidden="true"><path d="M30 2 a11 11 0 0 0 -10 15 L3 34 a4 4 0 0 0 7 7 L27 24 a11 11 0 0 0 15 -10 l-6 6 -7 -2 -2 -7 z" fill="#2e77b6"/></svg>
      <span class="service-title">Technical Solutions</span>
    </div>
    <p class="service-text">Aenean libero sapien, tempus quis adipiscing nec, hendrerit tincidunt ante. Integer vestibulum eros eu ipsum suscipit.</p>
  </div>

  <div class="abs service" style="left:90px;top:791px">
    <div class="service-head">
      <svg width="42" height="38" viewBox="0 0 42 38" aria-hidden="true"><rect x="1" y="1" width="40" height="36" fill="#fff" stroke="#2e77b6" stroke-width="2"/><rect x="1" y="1" width="40" height="6" fill="#2e77b6"/><rect x="14" y="20" width="14" height="11" fill="#2e77b6"/><path d="M17 20 v-4 a4 4 0 0 1 8 0 v4" fill="none" stroke="#2e77b6" stroke-width="2"/></svg>
      <span class="service-title">Security Services</span>
    </div>
    <p class="service-text">Aenean libero sapien, tempus quis adipiscing nec, hendrerit tincidunt ante. Integer vestibulum eros eu ipsum suscipit.</p>
  </div>
  <div class="abs service" style="left:365px;top:791px">
    <div class="service-head">
      <svg width="44" height="36" viewBox="0 0 44 36" aria-hidden="true"><g fill="none" stroke="#2e77b6" stroke-width="4" stroke-linecap="round"><path d="M3 12 a27 27 0 0 1 38 0"/><path d="M10 19 a17 17 0 0 1 24 0"/><path d="M17 26 a7 7 0 0 1 10 0"/></g><circle cx="22" cy="32" r="3" fill="#2e77b6"/></svg>
      <span class="service-title">Wireless Connections</span>
    </div>
    <p class="service-text">Aenean libero sapien, tempus quis adipiscing nec, hendrerit tincidunt ante. Integer vestibulum eros eu ipsum suscipit.</p>
  </div>
  <div class="abs service" style="left:637px;top:791px">
    <div class="service-head">
      <svg width="42" height="40" viewBox="0 0 42 40" aria-hidden="true"><circle cx="21" cy="11" r="10" fill="#2e77b6"/><path d="M2 40 q1 -16 19 -16 q18 0 19 16 z" fill="#2e77b6"/></svg>
      <span class="service-title">Consulting Services</span>
    </div>
    <p class="service-text">Aenean libero sapien, tempus quis adipiscing nec, hendrerit tincidunt ante. Integer vestibulum eros eu ipsum suscipit.</p>
  </div>
</section>

<div class="abs rule" style="top:928px"></div>

<div class="abs partners">
  <span>Wyndrel</span><span>Orbisane</span><span>Linqora</span><span>Sedrane</span><span>Tessavo</span><span>Norquil</span><span>Quilvanta</span><span>Pavrin</span><span>Strellix</span>
</div>

<section>
  <div class="abs news"></div>
  <div class="abs news-label">LATEST NEWS</div>
  <p class="abs news-text">Pellentesque ut purus at leo porttitor interdum at ut enim venenatis vehicula purus accumsa.<br>Aenean eu est vitae lectus congue dictum. <span class="news-date">January 17, 2014</span></p>
  <svg class="abs news-next" width="22" height="22" viewBox="0 0 22 22" aria-hidden="true"><circle cx="11" cy="11" r="11" fill="#bbb"/><path d="M9 6 L14 11 L9 16" fill="none" stroke="#fff" stroke-width="2.5"/></svg>
</section>

<footer>
  <div class="abs footer"></div>
  <div class="abs footer-links">Home<span>|</span>About us<span>|</span>IT Services<span>|</span>Backup Solutions<span>|</span>News<span>|</span>FAQ's<span>|</span>Contact us</div>
  <div class="abs copyright">Copyright &copy; 2013 &nbsp;Harlowe Cloud. &nbsp;All rights reserved.</div>
  <div class="abs social"><i></i><i></i><i></i><i></i></div>
  <div class="abs vendor"><i></i>VaultMerrin</div>
</footer>

</body>
</html>
```